Food truck menu design

Looking for a menu to be dissed for my toasted sandwich food truck. I have attached to logo and photo of the food truck for inspiration. if it can tie into them.
needing three sections, with titles:
CLASSICS
- classic one
. description
-Classic two
. Description
PREMIUM
- Premium one
. description
-Premium Two
. Description
-Premium Three
. Description
DESERT
-Desert one
. Description
-Desert two
.Description

also if it can be editable so I can change menu items and descriptions.

```html
<!DOCTYPE html>
<html lang="en">
<head>
<meta charset="utf-8">
<title>Food Truck Menu</title>
<link href="https://fonts.googleapis.com/css2?family=Montserrat:wght@400;500;700;800&family=Oswald:wght@500;600;700&display=swap" rel="stylesheet">
<style>
:root{
  --yellow:#fcc60b;
  --orange:#f5a11f;
  --maroon:#7a1b14;
  --brown:#4a1a10;
  --ink:#5a1a0e;
  --white:#ffffff;
  --paper:#ffffff;
}
*{margin:0;padding:0;box-sizing:border-box}
html,body{width:1200px;height:2642px;overflow:hidden;background:var(--paper)}
.menu-board{position:absolute;left:80px;top:801px;width:1040px;height:1040px;background:var(--yellow);overflow:hidden;font-family:'Montserrat',sans-serif;color:var(--ink)}
.abs{position:absolute}
.food-truck-title{left:100px;top:78px;width:150px;font-family:'Oswald',sans-serif;font-weight:700;color:var(--ink);line-height:.92;white-space:nowrap}
.food-truck-title .food{display:block;font-size:46px;letter-spacing:1px}
.food-truck-title .truck{display:block;font-size:60px;letter-spacing:-1px}
.truck-icon{left:262px;top:88px;width:100px;height:118px;border-radius:10px;background:linear-gradient(#c86068,#b8505a)}
.brand{left:400px;top:128px;width:260px;display:flex;align-items:center;gap:10px;justify-content:center}
.brand-dot{width:26px;height:26px;border-radius:50%;background:var(--maroon)}
.brand-name{font-family:'Montserrat',sans-serif;font-weight:800;font-size:30px;color:var(--maroon);white-space:nowrap}
.menu-title{left:680px;top:58px;font-family:'Oswald',sans-serif;font-weight:700;font-size:140px;line-height:1;color:var(--ink);letter-spacing:-2px}
.wave{left:0;width:1040px;height:24px}
.photo{border-radius:12px}
.photo-classics{left:130px;top:285px;width:195px;height:145px;background:radial-gradient(circle at 40% 50%,#c8784a,#f2d9a8 55%,#f5f5f5 75%)}
.photo-premium{left:580px;top:290px;width:285px;height:100px;border-radius:50px;background:radial-gradient(ellipse at 50% 45%,#9a4a24,#c06a2e 45%,#5c9a38 80%)}
.photo-cupcake{left:95px;top:745px;width:195px;height:105px;border-radius:8px;background:radial-gradient(ellipse at 45% 40%,#5a2e1e,#8a4a30 40%,#eeeeee 70%)}
.photo-icecream{left:710px;top:750px;width:140px;height:85px;border-radius:40px;background:radial-gradient(circle at 50% 40%,#8a5a40,#5a3020 60%,#c89a5a)}
.ribbon{height:56px}
.ribbon-label{position:absolute;inset:0;display:flex;align-items:center;justify-content:center;font-family:'Montserrat',sans-serif;font-weight:700;color:var(--white);font-size:38px}
.premium-box{left:500px;top:395px;width:455px;height:345px;background:var(--orange);border:2px solid var(--maroon);outline:2px solid var(--maroon);outline-offset:6px}
.item{position:absolute;width:var(--w)}
.item-name{font-weight:700;font-size:20px;color:var(--ink);line-height:1.2;white-space:nowrap}
.item-desc{font-weight:400;font-size:19px;color:var(--ink);line-height:1.5;white-space:nowrap}
.dots{position:absolute;height:0;border-top:3px dotted var(--ink)}
.price{position:absolute;width:64px;height:36px;background:var(--maroon);color:var(--yellow);font-family:'Oswald',sans-serif;font-weight:600;font-size:28px;line-height:36px;text-align:right;padding-right:6px;clip-path:polygon(0 0,100% 0,100% 100%,0 100%,12px 50%)}
.price sup{font-size:14px;vertical-align:10px;margin-right:1px}
.price-on-dark{background:var(--yellow);color:var(--brown)}
.dessert-band{left:85px;top:795px;width:835px;height:170px;background:var(--brown);border-radius:8px}
.dessert-title{left:85px;width:835px;top:812px;text-align:center;font-family:'Montserrat',sans-serif;font-weight:700;font-size:36px;color:var(--white)}
.dessert-item .item-name,.dessert-item .item-desc{color:var(--white)}
.bottom-band{left:0;top:975px;width:1040px;height:65px}
</style>
</head>
<body>
<main class="menu-board">

  <header>
    <div class="abs food-truck-title"><span class="food">FOOD</span><span class="truck">TRUCK</span></div>
    <div class="abs truck-icon" role="img" aria-label="Illustration of a food truck"></div>
    <div class="abs brand"><span class="brand-dot"></span><span class="brand-name">Toastie Lane</span></div>
    <h1 class="abs menu-title">MENU</h1>
  </header>

  <svg class="abs wave" style="top:250px" viewBox="0 0 1040 24"><path fill="none" stroke="var(--brown)" stroke-width="4" d="M0 12 q13 -10 26 0 t26 0 t26 0 t26 0 t26 0 t26 0 t26 0 t26 0 t26 0 t26 0 t26 0 t26 0 t26 0 t26 0 t26 0 t26 0 t26 0 t26 0 t26 0 t26 0 t26 0 t26 0 t26 0 t26 0 t26 0 t26 0 t26 0 t26 0 t26 0 t26 0 t26 0 t26 0 t26 0 t26 0 t26 0 t26 0 t26 0 t26 0 t26 0 t26 0"/></svg>

  <section class="classics">
    <div class="abs photo photo-classics" role="img" aria-label="Photo of steak with fries and vegetables"></div>
    <div class="abs ribbon" style="left:75px;top:443px;width:310px">
      <svg width="310" height="56" viewBox="0 0 310 56"><polygon points="0,24 30,24 30,56 0,56 14,40" fill="var(--maroon)" opacity=".85"/><polygon points="310,24 280,24 280,56 310,56 296,40" fill="var(--maroon)" opacity=".85"/><rect x="22" y="0" width="266" height="48" fill="var(--maroon)"/></svg>
      <div class="ribbon-label" style="bottom:8px">CLASSICS</div>
    </div>
    <div class="item" style="left:78px;top:508px;--w:310px"><div class="item-name">CAESAR SALAD</div><div class="item-desc">Parmesan cheese, lemon juice</div></div>
    <div class="price" style="left:393px;top:512px"><sup>$</sup>00</div>
    <div class="dots" style="left:78px;top:572px;width:380px"></div>
    <div class="item" style="left:78px;top:590px;--w:310px"><div class="item-name">MUSHROOM ROASTED BEEF...</div><div class="item-desc">Add here description.</div></div>
    <div class="price" style="left:393px;top:590px"><sup>$</sup>00</div>
    <div class="dots" style="left:78px;top:655px;width:380px"></div>
    <div class="item" style="left:78px;top:672px;--w:310px"><div class="item-name">LOADED BAKED POTATO</div><div class="item-desc">Add here description</div></div>
    <div class="price" style="left:393px;top:677px"><sup>$</sup>00</div>
    <div class="dots" style="left:78px;top:737px;width:380px"></div>
  </section>

  <section class="premium">
    <div class="abs premium-box"></div>
    <div class="abs photo photo-premium" role="img" aria-label="Photo of grilled chicken wings on salad"></div>
    <div class="abs ribbon" style="left:555px;top:400px;width:325px">
      <svg width="325" height="56" viewBox="0 0 325 56"><polygon points="0,20 30,20 30,52 0,52 14,36" fill="var(--maroon)" opacity=".85"/><polygon points="325,20 295,20 295,52 325,52 311,36" fill="var(--maroon)" opacity=".85"/><rect x="22" y="0" width="281" height="44" fill="var(--maroon)"/></svg>
      <div class="ribbon-label" style="bottom:12px">PREMIUM</div>
    </div>
    <div class="item" style="left:510px;top:475px;--w:300px"><div class="item-name">CHICKEN SPICY</div><div class="item-desc">Dolore ut cupitat</div></div>
    <div class="price" style="left:823px;top:477px"><sup>$</sup>00</div>
    <div class="dots" style="left:510px;top:538px;width:380px"></div>
    <div class="item" style="left:510px;top:558px;--w:300px"><div class="item-name">BBQ BEEF</div><div class="item-desc">Mollit aute ud laty</div></div>
    <div class="price" style="left:823px;top:555px"><sup>$</sup>00</div>
    <div class="dots" style="left:510px;top:620px;width:380px"></div>
    <div class="item" style="left:510px;top:640px;--w:300px"><div class="item-name">VEGETARIAN</div><div class="item-desc">Add here description</div></div>
    <div class="price" style="left:823px;top:647px"><sup>$</sup>00</div>
    <div class="dots" style="left:510px;top:702px;width:380px"></div>
  </section>

  <section class="dessert">
    <div class="abs dessert-band"></div>
    <div class="abs photo photo-cupcake" role="img" aria-label="Photo of chocolate cupcake dessert"></div>
    <div class="abs photo photo-icecream" role="img" aria-label="Photo of chocolate ice cream in a cone bowl"></div>
    <h2 class="abs dessert-title">DESERT</h2>
    <div class="item dessert-item" style="left:133px;top:868px;--w:160px"><div class="item-name">CUPCAKE</div><div class="item-desc">Dolore addatat</div></div>
    <div class="price price-on-dark" style="left:298px;top:877px"><sup>$</sup>00</div>
    <div class="item dessert-item" style="left:399px;top:868px;--w:160px"><div class="item-name">CHEESCAKE</div><div class="item-desc">Dolore addatat</div></div>
    <div class="price price-on-dark" style="left:565px;top:877px"><sup>$</sup>00</div>
    <div class="item dessert-item" style="left:665px;top:868px;--w:160px"><div class="item-name">ICECREAM</div><div class="item-desc">Dolore addatat</div></div>
    <div class="price price-on-dark" style="left:830px;top:877px"><sup>$</sup>00</div>
  </section>

  <svg class="abs bottom-band" viewBox="0 0 1040 65" preserveAspectRatio="none"><path fill="var(--brown)" d="M0 30 q20 -14 40 0 t40 0 t40 0 t40 0 t40 0 t40 0 t40 0 t40 0 t40 0 t40 0 t40 0 t40 0 t40 0 t40 0 t40 0 t40 0 t40 0 t40 0 t40 0 t40 0 t40 0 t40 0 t40 0 t40 0 t40 0 t40 0 L1040 65 L0 65 Z"/></svg>

</main>
</body>
</html>
```